Fast Money - Simple Book Cover Design

Hello,

I am in need of a cover for my new book. The Book Title Is

"Standing Growth - Keys to Glowing Customer Ratings That Fill The Calendar and Draw Fresh Clients Through Every Entrance!"

Author: Fireman Dale Orsworth

What I want: This is a book for businesses on improving their online reputation. I want to have 5 Stars on the cover. You can look at this quarvex search for ideas of what I am meaning.....

(copy and paste)

http://www.quarvex-find.example/search?q=5+star+online+reviews&mode=images&ref=kx7Lp2QwZt9 (copy and paste)

I am open to different color schemes for the book. I am partial to dark blues if you make it look good. Here is another book that I really like the cover of....

http://www.brindlemart.example/Clipwave-Tactics-Earning-Promotion-ebook/item/Z93KT4WQPX

I want the cover BOLD and to STAND OUT.

I am looking for a design to help establish me as an authority for online reputation marketing. This book will be both in Pagely format and be used in print as well.

I am open to questions....

Thanks!

Dale

Reason: I don't believe we have received the right designs. I am going to give everyone more time...

Reason: Hi everyone, I had some stuff come up and was not able to be involved in this project. I am extending because we have not seen the exact thing we want and need time to work with designers to get it right. Thanks Dale

Reason: I am currently traveling and can't wrap this up until I get back.

Target Market(s)

Business Owners

Industry/Entity Type

Business

Requirements
Must have
• Title and Subtitle

Author Name

5 Stars Images....
Nice to have
• Creativity

Bold and stand out

Professional

Should not have
• thin text, small to read text, lame graphics,

```html
<!DOCTYPE html>
<html lang="en">
<head>
<meta charset="utf-8">
<title>Standing Growth – Book Cover</title>
<link href="https://fonts.googleapis.com/css2?family=Anton&family=Quicksand:wght@700&display=swap" rel="stylesheet">
<style>
  :root {
    --navy: #140a5e;
    --navy-glow: #2a2290;
    --title-band: #5a4446;
    --cream: #fdf0c4;
    --gold: #fcc82a;
    --white: #ffffff;
    --sea-light: #6a8fd0;
    --sea-mid: #4f79c4;
    --sea-deep: #3e63ad;
    --author-ink: #3a2f87;
    --star: #fff5da;
  }
  * { margin: 0; padding: 0; box-sizing: border-box; }
  html, body { width: 900px; height: 1200px; overflow: hidden; background: var(--white); }
  .cover {
    position: relative;
    width: 900px;
    height: 1200px;
    overflow: hidden;
    background: var(--white);
  }
  .header {
    position: absolute;
    left: 0; top: 0;
    width: 900px; height: 326px;
    background: radial-gradient(circle at 450px 150px, var(--navy-glow) 0, var(--navy) 230px, var(--navy) 100%);
  }
  .title-band {
    position: absolute;
    left: 0; top: 98px;
    width: 900px; height: 150px;
    background: var(--title-band);
    display: flex;
    align-items: center;
    justify-content: center;
  }
  .title {
    font-family: 'Quicksand', sans-serif;
    font-weight: 700;
    font-size: 92px;
    color: var(--cream);
    white-space: nowrap;
    letter-spacing: 0;
    line-height: 1;
  }
  .gold-rule-top {
    position: absolute;
    left: 0; top: 334px;
    width: 900px; height: 19px;
    background: var(--gold);
  }
  .subtitle-panel {
    position: absolute;
    left: 0; top: 355px;
    width: 900px; height: 630px;
    background:
      radial-gradient(ellipse at 20% 30%, var(--sea-light) 0, transparent 45%),
      radial-gradient(ellipse at 80% 70%, var(--sea-deep) 0, transparent 50%),
      var(--sea-mid);
    display: flex;
    align-items: center;
    justify-content: center;
  }
  .subtitle {
    font-family: 'Anton', sans-serif;
    font-size: 66px;
    line-height: 88px;
    color: var(--white);
    text-align: center;
    width: 680px;
  }
  .author-band {
    position: absolute;
    left: 0; top: 985px;
    width: 900px; height: 200px;
    background: var(--gold);
  }
  .author {
    position: absolute;
    left: 0; top: 16px;
    width: 900px;
    text-align: center;
    font-family: 'Quicksand', sans-serif;
    font-weight: 700;
    font-size: 62px;
    line-height: 1;
    color: var(--author-ink);
  }
  .rating-stars {
    position: absolute;
    left: 175px; top: 84px;
  }
  .gold-rule-bottom {
    position: absolute;
    left: 0; top: 1191px;
    width: 900px; height: 9px;
    background: var(--gold);
  }
</style>
</head>
<body>
  <div class="cover">
    <div class="header" role="img" aria-label="Deep navy backdrop with a faint glowing geometric sphere"></div>
    <div class="title-band">
      <h1 class="title">Standing Growth</h1>
    </div>
    <div class="gold-rule-top"></div>
    <div class="subtitle-panel" role="img" aria-label="Blue painted abstract texture behind the subtitle">
      <p class="subtitle">Keys to Glowing Customer Ratings That Fill The Calendar and Draw Fresh Clients Through Every Entrance!</p>
    </div>
    <div class="author-band">
      <p class="author">Fireman Dale Orsworth</p>
      <svg class="rating-stars" width="550" height="112" viewBox="0 0 550 112" aria-label="Five star rating">
        <defs>
          <polygon id="star" points="55,0 68,40 110,40 76,65 89,105 55,80 21,105 34,65 0,40 42,40"/>
        </defs>
        <g fill="var(--star)">
          <use href="#star" x="0" y="3"/>
          <use href="#star" x="110" y="3"/>
          <use href="#star" x="220" y="3"/>
          <use href="#star" x="330" y="3"/>
          <use href="#star" x="440" y="3"/>
        </g>
      </svg>
    </div>
    <div class="gold-rule-bottom"></div>
  </div>
</body>
</html>
```